Business Card Design for Boutique Agriculture Consulting Practice

Develop a modern Business card design using uploaded logos . Using the color specs 6C344F rgb(108, 52, 79) The fonts are trajan pro and eurostile. The business owner is a woman and should have a hint of femininity. This is what is behind the naming of the company: Rock roads are synonymous with the rural US landscape, where the corn grows and the cattle graze or for Fern Gully Advisory home. But don’t let the dust get in your eyes, rock roads have edge and are often the only path to a spectacular destination. To navigate them one must know where they are going, have the courage to take a new path and the willingness to adjust their plans to get there.
Target Market(s)
Marketing Professionals
Industry/Entity Type
Agriculture
Contact Information for Business Card
Maribeth Tolland
Title: Founder and CEO
Address: 20473 Wesley Lane, Olathe Kansas 66218
Email: mt@ferngullyadvisory.com
Phone: 317.554.2019
Website: www.ferngullyadvisory.com
Font styles to use
Other font styles liked:
- trajan pro and eurostile
Requirements
Must have
- Please use the correct color specs. Logo color specs are 6C344F rgb(108, 52, 79) The fonts are trajan pro and eurostile. Name, email and phone be the most important information included on the card
Should not have
- additional graphics

```html
<!DOCTYPE html>
<html lang="en">
<head>
<meta charset="utf-8">
<title>Fern Gully Advisory – Business Card</title>
<link href="https://fonts.googleapis.com/css2?family=Cinzel:wght@400;600&family=Questrial&display=swap" rel="stylesheet">
<style>
  :root {
    --plum: #6C344F;
    --plum-light: #7a3d5b;
    --paper: #ffffff;
    --paper-shade: #f1f1f1;
    --backdrop: #3a3a3a;
    --ink-soft: #8a6a7a;
  }
  * { margin: 0; padding: 0; box-sizing: border-box; }
  html, body {
    width: 1200px;
    height: 900px;
    overflow: hidden;
    background: var(--backdrop);
  }
  .canvas {
    position: relative;
    width: 1200px;
    height: 900px;
  }
  .card {
    position: absolute;
    left: 300px;
    width: 600px;
    height: 343px;
    box-shadow: 0 10px 24px rgba(0,0,0,0.45);
  }

  /* Front side */
  .card--front {
    top: 70px;
    background: linear-gradient(135deg, var(--plum-light), var(--plum));
    color: var(--paper);
  }
  .card--front .brand-name {
    position: absolute;
    left: 0; right: 0;
    top: 120px;
    text-align: center;
    font-family: "Cinzel", serif;
    font-weight: 600;
    font-size: 34px;
    letter-spacing: 1px;
    color: var(--paper);
  }
  .card--front .website {
    position: absolute;
    left: 0; right: 0;
    bottom: 52px;
    text-align: center;
    font-family: "Questrial", sans-serif;
    font-size: 14px;
    letter-spacing: 0.5px;
    color: var(--paper);
  }

  /* Back side */
  .card--back {
    top: 487px;
    background: linear-gradient(160deg, var(--paper) 55%, var(--paper-shade));
    color: var(--plum);
  }
  .card--back .brand-name {
    position: absolute;
    left: 0; right: 0;
    top: 40px;
    text-align: center;
    font-family: "Cinzel", serif;
    font-weight: 600;
    font-size: 26px;
    letter-spacing: 1px;
    color: var(--plum);
  }
  .identity {
    position: absolute;
    right: 330px;
    top: 150px;
    text-align: right;
  }
  .identity .person-name {
    font-family: "Cinzel", serif;
    font-weight: 600;
    font-size: 24px;
    color: var(--plum);
    line-height: 1.1;
  }
  .identity .person-title {
    font-family: "Questrial", sans-serif;
    font-size: 14px;
    color: #555;
    margin-top: 4px;
  }
  .divider {
    position: absolute;
    left: 292px;
    top: 136px;
    width: 1.5px;
    height: 82px;
    background: var(--plum);
  }
  .contacts {
    position: absolute;
    left: 312px;
    top: 138px;
    list-style: none;
    font-family: "Questrial", sans-serif;
    font-size: 14px;
    color: var(--plum);
  }
  .contacts li {
    display: flex;
    align-items: center;
    gap: 8px;
    height: 26px;
  }
  .contacts svg { width: 13px; height: 13px; fill: var(--plum); flex: none; }
  .address {
    position: absolute;
    left: 0; right: 0;
    bottom: 48px;
    display: flex;
    justify-content: center;
    align-items: center;
    gap: 8px;
    font-family: "Questrial", sans-serif;
    font-size: 14px;
    color: var(--plum);
  }
  .address svg { width: 12px; height: 16px; fill: var(--plum); }
</style>
</head>
<body>
<main class="canvas">

  <section class="card card--front" aria-label="Card front">
    <div class="brand-name">Fern Gully Advisory</div>
    <div class="website">www.ferngullyadvisory.com</div>
  </section>

  <section class="card card--back" aria-label="Card back">
    <div class="brand-name">Fern Gully Advisory</div>

    <div class="identity">
      <div class="person-name">Maribeth Tolland</div>
      <div class="person-title">Founder and CEO</div>
    </div>

    <div class="divider"></div>

    <ul class="contacts">
      <li>
        <svg viewBox="0 0 24 24" aria-hidden="true"><path d="M6.6 10.8a15.1 15.1 0 0 0 6.6 6.6l2.2-2.2a1 1 0 0 1 1-.25 11.4 11.4 0 0 0 3.6.57 1 1 0 0 1 1 1V20a1 1 0 0 1-1 1A17 17 0 0 1 3 4a1 1 0 0 1 1-1h3.5a1 1 0 0 1 1 1c0 1.25.2 2.45.57 3.6a1 1 0 0 1-.25 1z"/></svg>
        317.554.2019
      </li>
      <li>
        <svg viewBox="0 0 24 24" aria-hidden="true"><path d="M2 5h20v14H2z M2 5l10 8 10-8" fill="none" stroke="#6C344F" stroke-width="0"/><path d="M2 5h20v2l-10 7L2 7z"/><path d="M2 9l10 7 10-7v10H2z"/></svg>
        mt@ferngullyadvisory.com
      </li>
      <li>
        <svg viewBox="0 0 24 24" aria-hidden="true"><circle cx="12" cy="12" r="10"/><path d="M2 12h20M12 2c3 3 3 17 0 20M12 2c-3 3-3 17 0 20" stroke="#fff" stroke-width="1.4" fill="none"/></svg>
        www.ferngullyadvisory.com
      </li>
    </ul>

    <div class="address">
      <svg viewBox="0 0 24 32" aria-hidden="true"><path d="M12 0C5.4 0 0 5.4 0 12c0 9 12 20 12 20s12-11 12-20C24 5.4 18.6 0 12 0zm0 17a5 5 0 1 1 0-10 5 5 0 0 1 0 10z"/></svg>
      20473 Wesley Lane, Olathe Kansas 66218
    </div>
  </section>

</main>
</body>
</html>
```